Larkspur Homes - wanted BRILLIANT website design for our new property investing company

We need a website design for our new company based in Bristol, England, UK called "Larkspur Homes". We help buy people property who are in financial difficulty or who are needing to sell their property quickly for reasons such as death, divorce/separation, relocation, emigration.

We have a logo being designed incorporating strawberry and property (so red and green). We would like designs to communicate an elegant ,professional, approachable, friendly
fresh clean but also warm appealing appearance
Not too busy
Website consistent with logo and company name i.e. colour scheme

Please use our word document for content as a guide but use professional judgement for minor alterations if you feel they would benefit the site/structure etc

Please ask at any time if not sure

Target Market(s)

Adult british population, those that have a mortgage / loan / own property

Industry/Entity Type

Financial

Font styles to use
Serif
Sans Serif
Decorative

Colors
0692cd
33b7a4
acd036
fbee3e
3176b5
886aae
a6479a
e567a6
eb1f27

Requirements
Must have
• This must not look like a template website we are looking for UNIQUE please!
Nice to have
• Bristol pictures instead of generic, or colourful line drawings/comic drawings of houses/property/keys/happy people.....
Should not have
• An obvious off the shelf template design

```html
<!DOCTYPE html>
<html lang="en">
<head>
<meta charset="utf-8">
<title>Larkspur Homes</title>
<link href="https://fonts.googleapis.com/css2?family=Montserrat:wght@700&family=Raleway:wght@300&family=Roboto+Condensed:ital,wght@0,400;0,700;1,700&family=Arimo:wght@400;700&display=swap" rel="stylesheet">
<style>
:root{
  --green:#4cb52a;
  --green-dark:#3a9a1c;
  --red:#d4262b;
  --nav:#2c3135;
  --panel-dark:#2f3d3e;
  --page:#f6f6f6;
  --aside:#e9e9e9;
  --footer:#151515;
  --text:#1c1c1c;
  --field:#e6e6e6;
}
*{margin:0;padding:0;box-sizing:border-box}
html,body{width:842px;height:1200px;overflow:hidden}
body{position:relative;background:var(--page);font-family:"Arimo",Arial,sans-serif;color:var(--text)}
.abs{position:absolute}

/* header + hero */
.hero-photo{left:0;top:0;width:842px;height:395px;
  background:linear-gradient(180deg,#5d6166 0%,#6a5f55 30%,#7a5333 55%,#3f3a33 78%,#6f6a5f 100%)}
.top-rule{left:0;top:0;width:842px;height:5px;background:var(--green)}
.hero-rule{left:0;top:395px;width:842px;height:5px;background:var(--green)}
.contact-pill{left:489px;top:4px;width:229px;height:22px;background:var(--green);color:#fff;font-size:10px;display:flex;align-items:center;gap:6px;padding:0 6px}
.contact-pill .sep{width:1px;height:14px;background:rgba(255,255,255,.5);margin:0 4px}
.brand{left:132px;top:22px;font-family:"Montserrat",sans-serif;font-weight:700;font-size:19px;color:#fff;letter-spacing:.2px}
.nav{left:0;top:66px;width:842px;height:42px;background:rgba(40,44,48,.88)}
.nav ul{list-style:none;display:flex;position:absolute;left:180px;top:0;height:42px}
.nav li{font-size:8.5px;color:#fff;line-height:42px;padding:0 12.5px}
.nav li.active{background:var(--red);padding:0 8px}
.welcome{left:231px;top:255px;width:380px;height:78px;background:rgba(40,44,44,.7);text-align:center}
.welcome .line1{font-family:"Raleway",sans-serif;font-weight:300;font-size:32px;color:#fff;letter-spacing:1px;line-height:40px;margin-top:2px}
.welcome .line2{font-family:"Montserrat",sans-serif;font-weight:700;font-size:31px;color:var(--green);line-height:36px}
.slide-arrow{top:279px;width:34px;height:32px;background:var(--red)}
.slide-arrow svg{display:block}

/* intro */
.intro-title{left:138px;top:429px;width:320px;font-family:"Arimo",sans-serif;font-weight:700;font-size:15.5px;line-height:19px;color:var(--red)}
.intro-lead{left:139px;top:477px;font-family:"Roboto Condensed",sans-serif;font-weight:700;font-size:11.5px}
.services{left:139px;top:497px;list-style:none;font-family:"Roboto Condensed",sans-serif;font-size:11px;line-height:16.6px}
.services li::before{content:"• "}

/* contact form */
.form-shadow{left:142px;top:946px;width:328px;height:24px;background:radial-gradient(ellipse at 50% 20%,rgba(0,0,0,.6),rgba(0,0,0,0) 70%)}
.contact-form{left:127px;top:672px;width:357px;height:282px;background:var(--panel-dark);border:1px solid #1d2626}
.form-title{left:12px;top:9px;font-family:"Roboto Condensed",sans-serif;font-size:18px;color:var(--green)}
.field-label{width:93px;text-align:right;font-size:9.5px;color:#fff}
.field{left:103px;width:214px;height:21px;background:var(--field)}
.btn-small{left:103px;top:248px;width:47px;height:18px;border-radius:3px;background:linear-gradient(#5ccb36,var(--green-dark));color:#fff;font-size:9px;font-weight:700;text-align:center;line-height:18px}

/* help panel */
.help{left:516px;top:432px;width:188px;height:523px;background:var(--aside);border:1px solid #cfcfcf}
.help-title{left:10px;top:8px;font-family:"Arimo",sans-serif;font-weight:700;font-size:17.5px;color:#555}
.help-item{left:7px;width:172px;height:23px;background:#fff;border:1px solid #c9c9c9;font-family:"Roboto Condensed",sans-serif;font-size:9px;color:#444;line-height:21px;padding-left:7px}
.btn-big{left:38px;top:484px;width:111px;height:24px;background:linear-gradient(#5ccb36,var(--green-dark));color:#fff;font-family:"Roboto Condensed",sans-serif;font-style:italic;font-weight:700;font-size:14px;text-align:center;line-height:24px;letter-spacing:.5px}

/* footer */
.footer-bar{left:0;top:1016px;width:842px;height:28px;background:var(--red)}
.footer-bar span{position:absolute;top:0;line-height:28px;font-size:8.5px;color:#fff}
.footer{left:0;top:1044px;width:842px;height:156px;background:var(--footer);color:#fff}
.footer-brand{left:138px;top:32px;font-family:"Montserrat",sans-serif;font-weight:700;font-size:13.5px;color:#fff}
.memberships{left:138px;top:56px;font-size:8.5px;line-height:12px}
.follow{left:138px;top:108px;font-size:8.5px;display:flex;align-items:center;gap:8px}
.social{width:20px;height:20px;border-radius:2px}
.social.one{background:#3b5a9a}
.social.two{background:#3fa9e0}
.map{left:337px;top:18px;width:185px;height:113px;background:linear-gradient(135deg,#dfe6d5,#e9e3c9 50%,#d8d6cc)}
.contact-heading{right:137px;top:31px;font-family:"Arimo",sans-serif;font-weight:700;font-size:12.5px;color:var(--green);letter-spacing:.5px}
.contact-lines{right:137px;top:49px;text-align:right;font-size:10px;line-height:13px}
</style>
</head>
<body>

<header>
  <div class="abs hero-photo" role="img" aria-label="Photo of a modern timber and glass house lit at dusk"></div>
  <div class="abs top-rule"></div>
  <div class="abs contact-pill">
    <svg width="11" height="8" viewBox="0 0 11 8"><rect x=".5" y=".5" width="10" height="7" fill="none" stroke="#fff"/><path d="M.5 .5 5.5 4.5 10.5 .5" fill="none" stroke="#fff"/></svg>
    <span>info@larkspur-homes.co.uk</span>
    <span class="sep"></span>
    <svg width="9" height="10" viewBox="0 0 9 10"><path d="M2 0 4 3 3 4C3.5 5.5 4.5 6.5 6 7L7 6 9 8 7.5 10C3.5 9.5.5 6.5 0 2.5Z" fill="#fff"/></svg>
    <span>07700900418</span>
  </div>
  <div class="abs brand">LARKSPUR HOMES</div>
  <nav class="abs nav">
    <ul>
      <li class="active">Home</li>
      <li>Sell Your Property Fast</li>
      <li>Rent Your Property Fast</li>
      <li>Common Questions</li>
      <li>About Us</li>
      <li>Contact Us</li>
    </ul>
  </nav>
  <div class="abs welcome">
    <div class="line1">WELCOME TO</div>
    <div class="line2">LARKSPUR HOMES</div>
  </div>
  <div class="abs slide-arrow" style="left:197px"><svg width="34" height="32"><path d="M20 9 12 16 20 23" fill="none" stroke="#fff" stroke-width="1.5"/></svg></div>
  <div class="abs slide-arrow" style="left:612px"><svg width="34" height="32"><path d="M14 9 22 16 14 23" fill="none" stroke="#fff" stroke-width="1.5"/></svg></div>
  <div class="abs hero-rule"></div>
</header>

<main>
  <h1 class="abs intro-title">Do you want to sell or rent out your house quickly?</h1>
  <p class="abs intro-lead">We are a local family run property business who specialize in</p>
  <ul class="abs services">
    <li>Buying properties quickly</li>
    <li>Finding creative solutions to your property problems</li>
    <li>Property rental management</li>
    <li>Lettings to professional and student tenants</li>
    <li>Guaranteed rent and management schemes for landlords</li>
    <li>STOPPING repossessions</li>
    <li>Motivated sellers</li>
    <li>Chain fixing</li>
    <li>Negative equity problems</li>
  </ul>

  <div class="abs form-shadow"></div>
  <form class="abs contact-form">
    <div class="abs form-title">Contact form</div>
    <div class="abs field-label" style="top:40px">Your Name:</div>
    <div class="abs field" style="top:41px"></div>
    <div class="abs field-label" style="top:71px">Email Address:</div>
    <div class="abs field" style="top:72px"></div>
    <div class="abs field-label" style="top:102px">Phone Number:</div>
    <div class="abs field" style="top:103px"></div>
    <div class="abs field-label" style="top:132px">Property Address:</div>
    <div class="abs field" style="top:133px"></div>
    <div class="abs field-label" style="top:161px">Message:</div>
    <div class="abs field" style="top:163px;height:75px"></div>
    <div class="abs btn-small">SUBMIT</div>
  </form>

  <aside class="abs help">
    <div class="abs help-title">Who can we help?</div>
    <div class="abs help-item" style="top:38px">HOW TO STOP REPOSSESSION</div>
    <div class="abs help-item" style="top:69px">DIVORCE OR SEPARATION</div>
    <div class="abs help-item" style="top:100px">FINANCIAL PROBLEMS</div>
    <div class="abs help-item" style="top:132px">DON'T LIKE ESTATE AGENTS?</div>
    <div class="abs help-item" style="top:163px">PROPERTY NEEDING WORK</div>
    <div class="abs help-item" style="top:194px">RETIRING LANDLORDS</div>
    <div class="abs help-item" style="top:226px">NEGATIVE EQUITY</div>
    <div class="abs help-item" style="top:257px">OPPORTUNITY NOT TO BE MISSED!!</div>
    <div class="abs help-item" style="top:289px">GUARANTEED RENT SCHEME</div>
    <div class="abs help-item" style="top:321px">ILL HEALTH</div>
    <div class="abs help-item" style="top:352px">RELOCATING</div>
    <div class="abs help-item" style="top:383px">INHERITED PROPERTY</div>
    <div class="abs help-item" style="top:415px">CHAIN COLLAPSE</div>
    <div class="abs help-item" style="top:446px">TENANTED PROPERTY</div>
    <div class="abs btn-big">SUBMIT</div>
  </aside>
</main>

<div class="abs footer-bar">
  <span style="left:138px">About Us</span>
  <span style="left:205px">Contact Us</span>
</div>
<footer class="abs footer">
  <div class="abs footer-brand">LARKSPUR HOMES</div>
  <p class="abs memberships">RCPV (Royal College of Property Valuers),<br>NLG (National Landlords Guild),<br>The Housing Redress Panel</p>
  <div class="abs follow">FOLLOW US:<span class="social one"></span><span class="social two"></span></div>
  <div class="abs map" role="img" aria-label="Street map showing the office location"></div>
  <div class="abs contact-heading">CONTACT US</div>
  <p class="abs contact-lines">2014 Larkspur Homes Limited.<br>Reg No 4471093<br>07700900418<br>info@larkspur-homes.co.uk</p>
</footer>

</body>
</html>
```